Business Card for a Life Coaching Company

BRAVOPEAK is a Life Coaching company that was initiated to support people who want to transform thier life or ana aspect of it.
our slogan is : "Dream. Believe. Succeed"
our logo is uploaded.
The name of the company implies that leadership, strength and wisdom required to change your life.
We want an attractive business card that would give an impression of reliability, support and change. so we really want it unique. Here are some examples of unique cards:

http://www.cardcraftvault.example/2009/05/100-really-creative-business-cards/

BravoPeak is a life coaching organization focusing on individual transformation through the application of relevant and timeless principles of success.  BravoPeak believes that real, sustainable life transformations are brought about by tuning into the timeless wisdom we each carry in our hearts while boldy acting in the direction of our dreams.

Contacts on the card:
Address: 7 Tarek Nour El Dine Heliopolis Cairo Egypt
Tel: +202 24 71 38 52
Fax: +202 24 71 38 17
Mobile: +2 012 684 2097 (Dalia Soliman)
+2 0199915815 (Tariq Bhatti)

By the way, our temporary website is http://www.bravopeak.example

We have attached an .eps file with various configurations of our logo.

```html
<!DOCTYPE html>
<html lang="en">
<head>
<meta charset="utf-8">
<title>BravoPeak — Business Card</title>
<link rel="stylesheet" href="https://fonts.googleapis.com/css2?family=Great+Vibes&family=Open+Sans:ital,wght@0,300;0,400;1,400&display=swap">
<style>
  :root {
    --card-white: #ffffff;
    --brand-orange: #ef7b2c;
    --brand-orange-deep: #ec6f1c;
    --peach-soft: #fbd3b4;
    --peach-faint: #fde9da;
    --logo-grey: #8c8c8c;
    --text-dark: #4a4a4a;
    --text-muted: #8a8a8a;
  }
  * { margin: 0; padding: 0; box-sizing: border-box; }
  html, body {
    width: 1200px;
    height: 685px;
    overflow: hidden;
    background: var(--card-white);
  }
  .business-card {
    position: relative;
    width: 1200px;
    height: 685px;
    overflow: hidden;
    font-family: "Open Sans", Arial, sans-serif;
    background: linear-gradient(to bottom,
      var(--card-white) 0%,
      var(--card-white) 50%,
      var(--peach-faint) 68%,
      var(--peach-soft) 82%,
      var(--brand-orange) 97%,
      var(--brand-orange-deep) 100%);
  }
  .emblem-artwork {
    position: absolute;
    left: 700px;
    top: 0;
    width: 500px;
    height: 685px;
    background: radial-gradient(ellipse at 60% 45%,
      rgba(247, 176, 126, 0.55) 0%,
      rgba(249, 196, 158, 0.35) 45%,
      rgba(255, 255, 255, 0) 75%);
  }
  .brand-mark {
    position: absolute;
    left: 36px;
    top: 85px;
    width: 120px;
    height: 120px;
    border-radius: 50%;
    background: var(--brand-orange);
  }
  .brand-name {
    position: absolute;
    left: 175px;
    top: 30px;
    font-weight: 300;
    font-size: 100px;
    line-height: 110px;
    color: var(--logo-grey);
    letter-spacing: 1px;
  }
  .contact-block {
    position: absolute;
    right: 45px;
    top: 50px;
    text-align: right;
    color: var(--text-dark);
    font-size: 37px;
    line-height: 49px;
  }
  .contact-block .address-line + .contact-line { margin-top: 16px; }
  .contact-line { white-space: nowrap; }
  .person {
    position: absolute;
    left: 80px;
    top: 374px;
    width: 480px;
    text-align: center;
  }
  .person-name {
    font-size: 48px;
    color: var(--text-dark);
    line-height: 56px;
  }
  .person-role {
    margin-top: 6px;
    font-style: italic;
    font-size: 32px;
    color: var(--text-muted);
  }
  .slogan {
    position: absolute;
    left: 40px;
    top: 545px;
    font-family: "Great Vibes", cursive;
    font-size: 84px;
    color: var(--card-white);
    white-space: nowrap;
    text-shadow:
      -1px -1px 0 var(--brand-orange-deep),
       1px -1px 0 var(--brand-orange-deep),
      -1px  1px 0 var(--brand-orange-deep),
       1px  1px 0 var(--brand-orange-deep),
       2px  2px 3px rgba(180, 70, 10, 0.45);
  }
</style>
</head>
<body>
  <main class="business-card">
    <div class="emblem-artwork" role="img" aria-label="Large faint brand emblem decoration"></div>

    <div class="brand-mark" aria-hidden="true"></div>
    <div class="brand-name">BRAVO<br>PEAK</div>

    <div class="contact-block">
      <div class="contact-line address-line">418 Larkspur Avenue</div>
      <div class="contact-line address-line">Marlow, GA 30912</div>
      <div class="contact-line">Phone: (358)555-0147</div>
      <div class="contact-line">E-mail: NWhitfield@BravoPeak.example</div>
    </div>

    <div class="person">
      <div class="person-name">Nora Whitfield</div>
      <div class="person-role">Project Manager</div>
    </div>

    <div class="slogan">Dream. Believe. Succeed.</div>
  </main>
</body>
</html>
```